依頼詳細
神奈川県横浜市で営業する美容室です。

今年で8回目のクリスマスDM依頼となります。

小さいお子様から70代ぐらいの方まで幅広い世代にご利用いただいております。
なかでも30代40代の美意識の高い大人の女性をメインターゲットにしています。

サロンの雰囲気についてはHPを参考にご覧ください。

今年もクリスマスDMのポストカードデザインをお願いいたします。

美容室ですが、美容室っぽさはデザインの中に取り込まなくても結構です。

イメージ的には、
堅苦しくなく、
家族や友人から送られてきたのかな??
と感じるような、
女性目線のシンプルかつオシャレなデザインが希望です。

また、オリジナル性を重視しますので、
ロゴもしくは店名(lumina by kovra)をデザインの中に取り入れていただきたいです。

過去の作品なども参考にしていただけたらと思います。

宜しくお願いいたします。
記載項目
表面(切手を貼る側)デザインにコメント・年末年始のお休みのお知らせ・店名住所電話番号の記載をお願いします。手書きコメントスペースがほしいです。

【コメント】日頃のご愛顧、誠にありがとうございます。皆様の笑顔の為に素敵なヘアデザインと最高の満足をお届けできるように、技術の向上とサービスに努めてまいります。kovraスタッフ一同、心よりお待ちしております。
【年末年始休み】12/31(土)~1/4水)まで 5(木)より 通常営業
【住所など】 lumina by kovra 横浜市中区花咲台3-48
横浜グランテラス桜坂1F TEL045-323-9807
【URL】http://kovra.jp
裏面:ロゴもしくは店名(lumina by kovra)イラスト
希望イメージ
シンプル 複雑
単色 カラフル
暗い 明るい
日常 高級
遊び心 厳粛
未来的 伝統的
女性的 男性的
希望する色
設定なし
納品ファイル
• 高解像度JPG (.jpg)
• イラストレーター形式 (.ai)
補足説明
印刷を「プリモア」さんにお願いを予定しています。入稿前チェックガイドのご確認よろしくお願い致します。
https://help.primoa-print.com/guide/data-check-guide/?_ga=1.232949529.648707975.1475738051
■ 選んだ理由

切手をモチーフにカラフルなデザインとユーモアがあり、お客様に喜んでいただけるのではないかと思い、決めさせていただきました。ありがとうございました。

■ 提案者全員のお礼・コメント

ご提案頂いた皆様、今回も素敵なデザインばかりで少々選定に時間がかかり申し訳ございませんでした。一つに絞るのが難しく贅沢な悩みでした。また機会がございましたら、よろしくお願い申し上げます。

```html
<!DOCTYPE html>
<html lang="ja">
<head>
<meta charset="utf-8">
<title>lumina by kovra — Christmas postcard</title>
<link rel="stylesheet" href="https://fonts.googleapis.com/css2?family=Noto+Sans+JP:wght@400;500;700&family=Raleway:wght@400;500;600&display=swap">
<style>
  :root {
    --ink: #3f3f3f;
    --ink-soft: #6a6a6a;
    --rule: #9a9a9a;
    --frame: #8a8a8a;
    --paper: #ffffff;
    --band: #5a5a5a;
    --band-text: #ffffff;
    --art: #dcdcdc;
  }
  * { margin: 0; padding: 0; box-sizing: border-box; }
  html, body { width: 810px; height: 1200px; overflow: hidden; background: var(--paper); }
  .card {
    position: relative; width: 810px; height: 1200px; overflow: hidden;
    background: var(--paper); color: var(--ink);
    font-family: "Noto Sans JP", sans-serif;
  }
  .postcard-label {
    position: absolute; left: 356px; top: 34px;
    font-family: "Raleway", sans-serif; font-weight: 500;
    font-size: 28px; letter-spacing: 6px; color: var(--ink-soft); line-height: 1;
  }
  .postal-code { position: absolute; left: 356px; top: 96px; display: flex; align-items: center; }
  .postal-code .box {
    width: 48px; height: 70px; border: 4px solid var(--ink); margin-right: 5px;
  }
  .postal-code .box.first { border-width: 6px; }
  .postal-code .dash { width: 12px; height: 4px; background: var(--ink); margin-right: 5px; }
  .stamp-frame { position: absolute; left: 88px; top: 104px; width: 176px; height: 176px; }
  .stamp-art {
    position: absolute; left: 128px; top: 144px; width: 96px; height: 96px;
    background: var(--art); border-radius: 6px;
  }
  .greeting {
    position: absolute; left: 0; width: 810px; top: 620px; text-align: center;
    font-family: "Raleway", sans-serif; font-weight: 600; line-height: 1;
    font-size: 24px; letter-spacing: 5px; color: var(--ink);
  }
  .message-lines { position: absolute; left: 59px; top: 612px; width: 691px; }
  .message-lines span {
    display: block; height: 46px; border-bottom: 2px dashed var(--rule);
  }
  .comment {
    position: absolute; left: 59px; top: 836px; width: 700px;
    font-size: 18px; line-height: 34px; color: var(--ink); letter-spacing: 0.3px;
  }
  .holiday { position: absolute; left: 120px; top: 1012px; display: flex; align-items: center; }
  .holiday-tag {
    background: var(--band); color: var(--band-text);
    font-size: 17px; padding: 3px 20px 3px 14px; font-weight: 500;
    clip-path: polygon(0 0, 100% 0, 93% 50%, 100% 100%, 0 100%);
  }
  .holiday-dates { margin-left: 70px; font-size: 21px; font-weight: 700; }
  .holiday-resume { margin-left: 80px; font-size: 21px; font-weight: 700; }
  .day {
    display: inline-block; width: 21px; height: 21px; border-radius: 50%;
    background: var(--ink); color: var(--paper); font-size: 12px;
    line-height: 21px; text-align: center; vertical-align: 2px; margin: 0 3px;
  }
  .footer {
    position: absolute; left: 0; bottom: 0; width: 810px; height: 120px;
    background: var(--band); color: var(--band-text);
    display: flex; align-items: center;
  }
  .shop-name {
    width: 230px; padding-left: 26px; white-space: nowrap;
    font-family: "Raleway", sans-serif; font-weight: 500; font-size: 24px; letter-spacing: 0.5px;
    border-right: 2px solid rgba(255,255,255,0.6); line-height: 80px;
  }
  .shop-info { padding-left: 24px; font-size: 17px; line-height: 36px; }
  .contact-row { display: flex; align-items: center; gap: 26px; }
  .contact-row span { display: inline-flex; align-items: center; gap: 6px; }
</style>
</head>
<body>
<main class="card">
  <div class="postcard-label">POSTCARD</div>
  <div class="postal-code">
    <div class="box first"></div><div class="box"></div><div class="box"></div>
    <div class="dash"></div>
    <div class="box"></div><div class="box"></div><div class="box"></div><div class="box"></div>
  </div>

  <svg class="stamp-frame" viewBox="0 0 176 176">
    <g stroke="var(--frame)" stroke-width="2" fill="none">
      <rect x="8" y="8" width="160" height="160"/>
    </g>
    <g fill="var(--frame)">
      <circle cx="8" cy="8" r="8"/><circle cx="168" cy="8" r="8"/>
      <circle cx="8" cy="168" r="8"/><circle cx="168" cy="168" r="8"/>
    </g>
  </svg>
  <div class="stamp-art" role="img" aria-label="Line illustration of a reindeer in the stamp area"></div>

  <div class="greeting">Merry Chrimas</div>
  <div class="message-lines"><span></span><span></span><span></span><span></span></div>

  <p class="comment">日頃のご愛顧、誠にありがとうございます。<br>皆様の笑顔の為に素敵なヘアデザインと最高の満足をお届けできるように、技術の向上とサービスに努めてまいります。<br>kovra スタッフ一同、心よりお待ちしております。</p>

  <div class="holiday">
    <span class="holiday-tag">年末年始休み</span>
    <span class="holiday-dates">31<span class="day">土</span>～ 4<span class="day">水</span></span>
    <span class="holiday-resume">5<span class="day">木</span>より通常営業</span>
  </div>

  <footer class="footer">
    <div class="shop-name">lumina by kovra</div>
    <div class="shop-info">
      <div>横浜市中区花咲台3-48 横浜グランテラス桜坂1F</div>
      <div class="contact-row">
        <span>
          <svg width="18" height="18" viewBox="0 0 24 24" fill="#fff"><path d="M6.6 10.8a15.2 15.2 0 0 0 6.6 6.6l2.2-2.2a1 1 0 0 1 1-.25 11.4 11.4 0 0 0 3.6.57 1 1 0 0 1 1 1V20a1 1 0 0 1-1 1A17 17 0 0 1 3 4a1 1 0 0 1 1-1h3.5a1 1 0 0 1 1 1c0 1.25.2 2.45.57 3.57a1 1 0 0 1-.25 1z"/></svg>
          045-618-2734
        </span>
        <span>
          <svg width="20" height="16" viewBox="0 0 24 20" fill="none" stroke="#fff" stroke-width="2"><rect x="2" y="2" width="20" height="13" rx="1"/><line x1="8" y1="19" x2="16" y2="19"/></svg>
          http://kovra.jp
        </span>
      </div>
    </div>
  </footer>
</main>
</body>
</html>
```